Workplace Safety Consultancy Business needs business card design

We need a business card for a new business providing workplace health and safety consulting called 'Worksure Guard'. We will be providing small to medium sized businesses assistance with OH&S and HR matters to ensure that their employees and the public are safe in the workplace and that they are meeting their legislative requirements. Would like to see the words 'practical workplace safety solutions' on the card. Personal details on the back. It needs to be clean, smart and professional (no fluff). Would like to see a simple logo if possible as well. Have been looking at orange and black, but open to other ideas.
Updates
Thank you to those to have created designs for us so far! We are really impressed with the impact of the black and orange having now seen it. Would be great if any further designs used those colours. Cheers.

Thank you to everyone that submitted a design. Your work is of the highest quality and we had a hard decision deciding. Sorry if we didn't choose your design, but it just came down to the one that stood out to us personally. Cheers.

Target Market(s)
Small-Medium business owners in Queensland, Australia. Age 25-60 male and female. Initially targeting those in the trade type industries
Industry/Entity Type
Health
Look and feel
Each slider illustrates characteristics of the customer's brand and the style your logo design should communicate.

```html
<!DOCTYPE html>
<html lang="en">
<head>
<meta charset="UTF-8">
<title>Worksure Guard – Business Card</title>
<link href="https://fonts.googleapis.com/css2?family=Exo+2:wght@400;600;700&display=swap" rel="stylesheet">
<style>
  :root{
    --backdrop:#dcdde0;
    --card:#ffffff;
    --brand-orange:#f47b20;
    --brand-black:#1c1c1c;
    --text-grey:#4a4a4a;
    --on-orange:#ffffff;
    --shadow:rgba(0,0,0,.18);
  }
  *{margin:0;padding:0;box-sizing:border-box}
  html,body{width:1200px;height:894px;overflow:hidden}
  body{background:var(--backdrop);font-family:"Exo 2",sans-serif;position:relative}

  .card{
    position:absolute;top:292px;width:540px;height:309px;
    background:var(--card);box-shadow:0 6px 18px var(--shadow);overflow:hidden;
  }
  .card--front{left:40px}
  .card--back{left:620px}

  .corner-tab{position:absolute;top:0;right:0;background:var(--brand-black)}
  .card--front .corner-tab{width:130px;height:40px}
  .card--back .corner-tab{width:70px;height:100px}

  .wordmark{color:var(--brand-orange);font-weight:400;line-height:.95;letter-spacing:.5px}
  .card--front .wordmark{position:absolute;left:26px;top:22px;font-size:40px}
  .card--back .wordmark{position:absolute;left:0;right:0;top:112px;text-align:center;font-size:46px}

  .tagline{
    position:absolute;left:0;right:0;top:176px;text-align:center;
    color:var(--brand-black);font-weight:600;font-size:14px;
    letter-spacing:2.6px;text-transform:uppercase;
  }

  .person{position:absolute;left:262px;top:92px}
  .person__name{color:var(--brand-black);font-weight:700;font-size:22px;letter-spacing:1.5px;text-transform:uppercase}
  .person__title{color:var(--brand-orange);font-weight:600;font-size:15px;letter-spacing:1.2px;text-transform:uppercase;margin-top:1px}

  .contact-band{
    position:absolute;left:20px;top:152px;width:500px;height:132px;
    background:var(--brand-orange);border-radius:14px;display:flex;
  }
  .contact-band__cell{
    flex:1;display:flex;flex-direction:column;align-items:center;
    padding-top:16px;color:var(--on-orange);font-size:13px;line-height:1.45;text-align:center;
  }
  .contact-band__cell + .contact-band__cell{border-left:1.5px solid var(--on-orange)}
  .contact-band__icon{width:30px;height:30px;margin-bottom:14px}
</style>
</head>
<body>

<section class="card card--front" aria-label="Business card front">
  <div class="corner-tab"></div>
  <div class="wordmark">Worksure<br>Guard</div>
  <div class="person">
    <div class="person__name">Daniel Hart</div>
    <div class="person__title">Creative Director</div>
  </div>

  <div class="contact-band">
    <div class="contact-band__cell">
      <svg class="contact-band__icon" viewBox="0 0 30 30" aria-hidden="true">
        <path d="M4 11c0-4 5-6 11-6s11 2 11 6v2h-6v-3c-3-1-7-1-10 0v3H4z" fill="var(--on-orange)"/>
        <path d="M9 14h12l4 8v3H5v-3z" fill="none" stroke="var(--on-orange)" stroke-width="2" stroke-linejoin="round"/>
        <circle cx="15" cy="20" r="2.5" fill="var(--on-orange)"/>
      </svg>
      <span>014 552 8130</span>
      <span>014 552 8131</span>
    </div>
    <div class="contact-band__cell">
      <svg class="contact-band__icon" viewBox="0 0 30 30" aria-hidden="true" fill="none" stroke="var(--on-orange)" stroke-width="1.8">
        <circle cx="15" cy="15" r="12"/>
        <ellipse cx="15" cy="15" rx="5.5" ry="12"/>
        <line x1="3" y1="15" x2="27" y2="15"/>
        <path d="M5 9h20M5 21h20"/>
      </svg>
      <span>hello@mailbox.com</span>
      <span>www.worksureguard.com</span>
    </div>
    <div class="contact-band__cell">
      <svg class="contact-band__icon" viewBox="0 0 30 30" aria-hidden="true">
        <path d="M15 2a9 9 0 0 0-9 9c0 7 9 17 9 17s9-10 9-17a9 9 0 0 0-9-9z" fill="var(--on-orange)"/>
        <circle cx="15" cy="11" r="3.5" fill="var(--brand-orange)"/>
      </svg>
      <span>047,12th floor,Park</span>
      <span>Harbour Road QLD</span>
    </div>
  </div>
</section>

<section class="card card--back" aria-label="Business card back">
  <div class="corner-tab"></div>
  <div class="wordmark">Worksure Guard</div>
  <div class="tagline">Practical workplace safety solutions</div>
</section>

</body>
</html>
```